QV - menu design

Hi,

We require elegant menu design for upscale restaurant. Please find attached the logo and the menu items for your reference.

for inspiration, this is a good website: -
http://www.platewhisper.example/bellfoldnotes/about.php

We are very much open for Menu Size suggestions.

unfortunately the place is going under renovation, we don't have updated images to it. the closest look and feel to our place is http://varnelo.example ..

we are also open for creative options on the shape, the styles, etc. as long as it represents the fine dine feel ...

Thanks ...

Dear All,

We wouldlike to extend our apology for not being able to provide feedbacks on everysingle design. We were extremely busy and we have multiple contests opensimultaneously which makes the process even harder.

However,we would like to thank you all for the efforts you have put into designingour menu. It is very much appreciated …

We wishyou all success in your design ventures and we are quite positive that we willbe working with many of you on many projects in the soon future. 

Thanks & Regards,

TLG Team...

 

 

 

Industry/Entity Type

Restaurant

Requirements
Must have
• Please ensure that there are 'some' images in the menu ... this is very important.
Should not have
• IMPORTANT: -

1. Please DO NOT insert any currency sign to the menu
2. Please keep the prices of the menu at the end of the menu items descriptions NOT beside the menu item names. The font of the price should be similar to the menu item description and please DO NOT bold the numbers. the prices should be subtle.

Thank you ...

```html
<!DOCTYPE html>
<html lang="en">
<head>
<meta charset="utf-8">
<title>QV Café – Menu</title>
<link rel="stylesheet" href="https://fonts.googleapis.com/css2?family=Didact+Gothic&family=Poiret+One&display=swap">
<style>
  :root {
    --backdrop: #f4f3f0;
    --paper: #ffffff;
    --sand: #c6baa2;
    --sand-soft: #e6e0d4;
    --cocoa: #4b2f20;
    --ink: #2b2622;
    --rule: #ffffff;
  }
  * { box-sizing: border-box; margin: 0; padding: 0; }
  html, body {
    width: 1200px; height: 900px; overflow: hidden;
    background: var(--backdrop);
  }
  .board {
    position: relative; width: 1200px; height: 900px;
    display: flex; justify-content: center; align-items: center; gap: 90px;
  }
  .sheet {
    position: relative; width: 380px; height: 660px;
    background: var(--paper);
    box-shadow: 3px 4px 10px rgba(0,0,0,.18);
    overflow: hidden;
  }
  .edge-strip {
    position: absolute; top: 8px; bottom: 0; right: 0; width: 14px;
    background: var(--cocoa);
  }
  .flourish-area {
    position: absolute;
    background: radial-gradient(ellipse at 55% 45%, var(--sand-soft) 0%, rgba(230,224,212,.55) 45%, rgba(255,255,255,0) 75%);
  }

  /* Cover */
  .cover-band {
    position: absolute; top: 0; bottom: 0; left: 32px; width: 104px;
    background: var(--sand);
  }
  .cover-band::after {
    content: ""; position: absolute; top: 0; bottom: 0; left: 50%;
    border-left: 1.5px dashed var(--rule);
  }
  .cover .flourish-area { top: 30px; right: 20px; width: 240px; height: 600px; }
  .wordmark {
    position: absolute; left: 118px; top: 470px; text-align: center;
    font-family: "Poiret One", sans-serif; color: var(--ink);
  }
  .wordmark-name { font-size: 58px; letter-spacing: 8px; line-height: 1; }
  .wordmark-sub { font-size: 14px; letter-spacing: 6px; margin-top: 4px; }

  /* Breakfast page */
  .page-header {
    position: absolute; top: 30px; left: 0; right: 14px; height: 62px;
    background: var(--sand);
    font-family: "Poiret One", sans-serif; color: var(--rule);
    font-size: 30px; letter-spacing: 2px; text-transform: uppercase;
    padding: 8px 0 0 60px;
  }
  .page-header::after {
    content: ""; position: absolute; left: 0; right: 0; bottom: 12px;
    border-top: 1.5px dashed var(--rule);
  }
  .page .flourish-area { top: 240px; left: 0; width: 260px; height: 420px; }
  .menu-list {
    position: absolute; top: 120px; left: 44px; right: 44px;
    font-family: "Didact Gothic", sans-serif; color: var(--ink);
    list-style: none;
  }
  .menu-item { margin-bottom: 13px; }
  .item-name {
    font-size: 13px; font-variant: small-caps; letter-spacing: .5px;
    margin-bottom: 4px;
  }
  .item-desc {
    font-size: 8.5px; font-variant: small-caps; line-height: 1.45;
    letter-spacing: .3px; color: #463f38;
  }
  .page-mark {
    position: absolute; right: 34px; bottom: 22px; text-align: center;
    font-family: "Poiret One", sans-serif; color: var(--ink);
  }
  .page-mark .wordmark-name { font-size: 22px; letter-spacing: 4px; }
  .page-mark .wordmark-sub { font-size: 7px; letter-spacing: 3px; margin-top: 1px; }
</style>
</head>
<body>
<main class="board">

  <section class="sheet cover" aria-label="Menu cover">
    <div class="flourish-area" role="img" aria-label="Faint beige swirling flourish pattern"></div>
    <div class="cover-band"></div>
    <div class="edge-strip"></div>
    <div class="wordmark">
      <div class="wordmark-name">QV</div>
      <div class="wordmark-sub">CAFÉ</div>
    </div>
  </section>

  <section class="sheet page" aria-label="Breakfast menu page">
    <div class="flourish-area" role="img" aria-label="Faint beige swirling flourish pattern"></div>
    <h1 class="page-header">The Breakfast</h1>
    <div class="edge-strip"></div>
    <ul class="menu-list">
      <li class="menu-item">
        <h2 class="item-name">Butter Croissant</h2>
        <p class="item-desc">Served plain with a selection of two jams, a vanilla custard cream, a chocolate cream and butter curls. 36</p>
      </li>
      <li class="menu-item">
        <h2 class="item-name">Cheese Croissant</h2>
        <p class="item-desc">Crumbly freshly baked with cheese filling. 29</p>
      </li>
      <li class="menu-item">
        <h2 class="item-name">Daily Fresh Eggs</h2>
        <p class="item-desc">A choice of poached, scrambled, pan fried, omelet) all served with toasted bread, mushrooms, roasted tomatoes and chicken sausages. 59</p>
      </li>
      <li class="menu-item">
        <h2 class="item-name">Healthy Time</h2>
        <p class="item-desc">One choice of hot beverage from our cafe served with fruit salad, natural yoghurt, whole wheat bread vegetable sandwiches and sugar free biscuits selection. 49</p>
      </li>
      <li class="menu-item">
        <h2 class="item-name">Energy Time</h2>
        <p class="item-desc">One choice of hot beverage from our cafe served with finger chocolate muffins, poached egg with toasted bread and crispy beef bacon, crepe roll with goat cheese and honey and finger chocolate cream with salted cookies. 59</p>
      </li>
      <li class="menu-item">
        <h2 class="item-name">QV Time</h2>
        <p class="item-desc">One choice of hot beverage from our cafe served with our selection of scones, smoked salmon and avocado sandwich, roasted sausages sandwich, grilled vegetables sandwich, selection of our best biscuits. 59</p>
      </li>
      <li class="menu-item">
        <h2 class="item-name">The Arabic Breakfast</h2>
        <p class="item-desc">Choice of zattar manakish and cheese manakish, served with one choice of hot beverage from our cafe and fresh orange juice. 39</p>
      </li>
    </ul>
    <div class="page-mark">
      <div class="wordmark-name">QV</div>
      <div class="wordmark-sub">CAFÉ</div>
    </div>
  </section>

</main>
</body>
</html>
```